Freelance business trainer needs a new business card

My business is called Tbrite. I provide training in the workplace on management, coaching and mentoring, and customer service topics for a variety of businesses, colleges and private training providers, and teach on management programs. I need a professional but eye catching business card. Business colours grey and orange. My name Linda Marchbank; Tel 07853 416207; email lmarchbank@tbrite.co.uk; website www.tbrite.co.uk.
Happy to have some sort of logo on front and details on back or all on one side
Target Market(s)
SME businesses and colleges - workshops i run are for adults in the workplace
Industry/Entity Type
Training
Look and feel

```html
<!DOCTYPE html>
<html lang="en">
<head>
<meta charset="utf-8">
<title>Tbrite – Business Cards</title>
<link rel="stylesheet" href="https://fonts.googleapis.com/css2?family=Mulish:wght@400;600;800&display=swap">
<style>
  :root {
    --orange: #f7931e;
    --orange-light: #f9a94a;
    --grey: #6d6e70;
    --grey-dark: #5e5f61;
    --white: #f4f4f4;
    --paper: #ffffff;
    --backdrop: #d9dadc;
  }
  * { margin: 0; padding: 0; box-sizing: border-box; }
  html, body {
    width: 1200px; height: 800px; overflow: hidden;
    background: var(--backdrop);
    font-family: "Mulish", "Helvetica Neue", Arial, sans-serif;
  }
  .canvas {
    position: relative; width: 1200px; height: 800px;
    display: flex; align-items: center; justify-content: center; gap: 60px;
  }
  .card {
    position: relative; width: 520px; height: 336px; overflow: hidden;
    box-shadow: 0 6px 18px rgba(0,0,0,.18);
  }
  .card__circles { position: absolute; inset: 0; }

  /* Front */
  .card--front { background: var(--orange); }
  .card--front .band {
    position: absolute; left: 0; right: 0; bottom: 0; height: 58px;
    background: var(--white); border-top: 3px solid var(--grey);
  }
  .brand {
    position: absolute; font-weight: 600; letter-spacing: 1px; line-height: 1;
  }
  .card--front .brand {
    left: 150px; top: 84px; font-size: 92px; color: var(--grey);
  }
  .brand-dot {
    position: absolute; border-radius: 50%;
  }
  .card--front .brand-dot {
    left: 118px; top: 142px; width: 18px; height: 18px; background: var(--white);
  }
  .tagline {
    position: absolute; left: 40px; right: 40px; top: 218px;
    text-align: center; color: var(--white); font-size: 15.5px; letter-spacing: .6px;
  }

  /* Back */
  .card--back { background: var(--grey); }
  .card--back .band-top {
    position: absolute; left: 0; right: 0; top: 0; height: 44px;
    background: var(--white); border-bottom: 4px solid var(--orange);
  }
  .card--back .band-bottom {
    position: absolute; left: 0; right: 0; bottom: 0; height: 20px; background: var(--white);
  }
  .card--back .accent {
    position: absolute; left: 0; bottom: 20px; width: 90px; height: 4px; background: var(--orange);
  }
  .website {
    position: absolute; top: 12px; right: 28px;
    color: var(--orange); font-size: 17px; letter-spacing: 2.5px;
  }
  .contact {
    position: absolute; left: 30px; top: 70px; color: var(--white);
  }
  .contact__name {
    color: var(--orange); font-weight: 800; font-size: 22px; letter-spacing: 1px; text-transform: uppercase;
  }
  .contact__role, .contact__quals { font-size: 12px; line-height: 1.45; }
  .contact__lines { margin-top: 16px; font-size: 14px; line-height: 1.55; list-style: none; }
  .contact__lines .label { color: var(--orange); margin-right: 4px; }
  .address {
    position: absolute; left: 30px; bottom: 40px; color: var(--white);
    font-size: 15px; line-height: 1.45; font-style: normal;
  }
  .card--back .brand {
    right: 34px; bottom: 54px; font-size: 64px; color: var(--white);
  }
  .card--back .brand-dot {
    right: 236px; bottom: 58px; width: 14px; height: 14px; background: var(--orange);
  }
</style>
</head>
<body>
<main class="canvas">

  <section class="card card--front" aria-label="Card front">
    <svg class="card__circles" viewBox="0 0 520 336" aria-hidden="true">
      <circle cx="250" cy="40" r="140" fill="#ffffff" opacity=".12"/>
      <circle cx="330" cy="230" r="140" fill="#6d6e70" opacity=".1"/>
    </svg>
    <span class="brand-dot"></span>
    <span class="brand">Tbrite</span>
    <p class="tagline">Management, Business &amp; Customer Service Training</p>
    <div class="band"></div>
  </section>

  <section class="card card--back" aria-label="Card back">
    <svg class="card__circles" viewBox="0 0 520 336" aria-hidden="true">
      <circle cx="330" cy="250" r="110" fill="#ffffff" opacity=".06"/>
      <circle cx="440" cy="300" r="110" fill="#ffffff" opacity=".06"/>
    </svg>
    <div class="band-top"></div>
    <p class="website">www.tbrite.co.uk</p>

    <div class="contact">
      <h1 class="contact__name">Linda Marchbank</h1>
      <p class="contact__role">Owner/Lead Trainer</p>
      <p class="contact__quals">MCMI, MIFL, CertEd, PGCCM, TIOSH</p>
      <ul class="contact__lines">
        <li><span class="label">[T]</span>07853 416207</li>
        <li><span class="label">[E]</span>lmarchbank@tbrite.co.uk</li>
      </ul>
    </div>

    <address class="address">Maple Court<br>Fernley Lane<br>Ashby<br>RG31 4TP</address>

    <span class="brand-dot"></span>
    <span class="brand">Tbrite</span>

    <div class="accent"></div>
    <div class="band-bottom"></div>
  </section>

</main>
</body>
</html>
```